Domain Search Page and Results

We are looking for creative methods to display a domain registration search page, with many extensions. We are only looking for designs of the inside of the page and not for the frame around the page.
There are currently 4 categories and after pressing submit there is the results: however in the future there will be more categories (around 7 or 8) and domain extensions.
We would like creative methods to display the different (7-8) categories and extensions and also the results display.
The categories should be open/close-able.
We are planning to use JQuery and your suggestions for any movement will be appreciated.
We also would like creative ways to display the results.
Thank you.
Additions:
- It is not necessary to change the template/frame of the page. We are only looking for the search AND results display.
- We are looking for creative ideas and not necessary judging based on the actual design.
- We are basing the winner on how creatively it will be possible to display the search function AND results display. And to display creatively 7 or 8 categories with 100''s of domain extensions. The more creative and yet still user friendly the search functionality is, the chances of being selected will be higher.
- There will be 7 or 8 categories (and not just 4 as in the sample). The design must be able to extend to 7 or 8 categories. In some categories there are over 100 extensions. Creative ideas on how to sub categorize the extensions will be a bonus.

```html
<!DOCTYPE html>
<html lang="en">
<head>
<meta charset="utf-8">
<title>Kaito Domains – Domain Search</title>
<link rel="stylesheet" href="https://fonts.googleapis.com/css2?family=Noto+Sans:wght@400;700&display=swap">
<style>
  :root {
    --sky-top: #5ab8ee;
    --sky-bottom: #ffffff;
    --column-edge: #1e5d94;
    --nav-text: #1f4a63;
    --nav-bg-top: #ffffff;
    --nav-bg-bottom: #e3f0f8;
    --rule: #b8c4cc;
    --orange: #f7850f;
    --orange-light: #ffb13c;
    --title-red: #a80f0f;
    --alert-red: #e60000;
    --body-text: #444444;
    --link-blue: #3d7ab8;
    --panel-bg: #f4f4f4;
    --panel-edge: #d6d6d6;
    --panel-title: #3a6fcf;
    --hex-stroke: #222222;
    --hex-active: #b3b3b3;
    --sketch-fill: #ececec;
    --brand-red: #c41414;
  }
  * { box-sizing: border-box; margin: 0; padding: 0; }
  html, body { width: 1200px; height: 634px; overflow: hidden; }
  body {
    font-family: "Noto Sans", sans-serif;
    background: linear-gradient(to bottom, var(--sky-top) 0%, #9fd6f6 60%, var(--sky-bottom) 100%);
    position: relative;
  }
  .page {
    position: absolute; left: 202px; top: 0; width: 797px; height: 634px;
    background: #fff;
    border-left: 1px solid var(--column-edge);
    border-right: 1px solid var(--column-edge);
  }
  .site-header { position: relative; height: 86px; }
  .brand {
    position: absolute; left: 14px; top: 18px;
    display: flex; align-items: center; gap: 10px;
  }
  .brand-mark { width: 46px; height: 46px; border-radius: 50%; background: var(--brand-red); }
  .brand-name { font-size: 34px; font-weight: 700; color: #1a1a1a; letter-spacing: -0.5px; }
  .languages { position: absolute; top: 28px; left: 0; }
  .language {
    position: absolute; width: 40px; text-align: center;
    font-size: 11px; color: #8a8a8a; font-weight: 700;
  }
  .language-flag {
    display: block; width: 30px; height: 24px; margin: 0 auto 4px;
    background: #dde3ea; border: 1px solid #c5cbd2;
  }
  .nav {
    position: absolute; top: 86px; left: 0; width: 100%; height: 23px;
    background: linear-gradient(var(--nav-bg-top), var(--nav-bg-bottom));
    border-top: 1px solid #9cc5de; border-bottom: 1px solid #9cc5de;
  }
  .nav-item {
    position: absolute; top: 3px; font-size: 12.5px; font-weight: 700; color: var(--nav-text);
  }
  .control-panel {
    position: absolute; right: 1px; top: 0; width: 158px; height: 21px;
    background: linear-gradient(var(--orange-light), var(--orange));
    color: #fff; font-size: 12.5px; font-weight: 700; text-align: center; line-height: 21px;
  }
  .crumbs {
    position: absolute; top: 109px; left: 0; width: 100%; height: 25px;
    border-bottom: 1px solid var(--rule); font-size: 11.5px; color: #333;
  }
  .crumbs-trail { position: absolute; left: 15px; top: 5px; }
  .crumbs-trail a, .crumbs-account a { color: var(--link-blue); }
  .crumbs-account { position: absolute; right: 8px; top: 3px; font-size: 13px; }
  .crumbs-account strong a { color: var(--alert-red); }
  .search-area { position: absolute; left: 15px; top: 150px; width: 590px; }
  .search-title {
    font-size: 17px; font-weight: 700; color: var(--title-red);
    padding-bottom: 3px; border-bottom: 1px solid #cfcfcf;
  }
  .search-intro { margin-top: 6px; font-size: 13px; line-height: 17px; color: #555; width: 520px; }
  .domain-input {
    position: absolute; left: 15px; top: 253px; width: 139px; height: 20px;
    border: 2px solid #7a8fc8; font: 12px "Noto Sans", sans-serif; padding: 0 2px;
  }
  .tld-chain { position: absolute; left: 0; top: 0; }
  .tld-chain text { font: 700 10px "Noto Sans", sans-serif; fill: #111; text-anchor: middle; }
  .concept-sketch { position: absolute; background: var(--sketch-fill); }
  .sidebar { position: absolute; left: 606px; top: 151px; width: 176px; }
  .promo {
    height: 121px; border: 1px solid #c7b59a; padding: 10px 8px;
    background: linear-gradient(#ffa02e, var(--orange));
    position: relative; color: #fff; font-size: 16px; line-height: 18px; font-weight: 700;
  }
  .promo-globe { position: absolute; right: 8px; top: 8px; width: 62px; height: 62px; border-radius: 50%; background: #d9d9d9; }
  .promo-button {
    position: absolute; left: 10px; bottom: 6px; width: 154px; height: 24px; border-radius: 12px;
    background: #3d5a8a; color: #fff; font-size: 12px; text-align: center; line-height: 24px;
  }
  .panel {
    margin-top: 24px; border: 1px solid var(--panel-edge); border-radius: 6px;
    background: var(--panel-bg); padding: 10px 11px; font-size: 11px; line-height: 17px; color: var(--body-text);
  }
  .panel-head { position: relative; height: 68px; }
  .panel-title { font-size: 19px; font-weight: 700; color: var(--panel-title); line-height: 24px; }
  .panel-icon { position: absolute; right: -2px; top: -2px; width: 52px; height: 52px; background: #3b6f9c; border-radius: 4px; }
  .badge-new { display: block; width: 22px; height: 9px; background: #c9823b; margin-top: 6px; }
  .panel p { margin-top: 17px; }
  .panel .panel-head + p { margin-top: 6px; }
  .panel .highlight { color: var(--alert-red); font-weight: 700; }
  .news { height: 238px; }
  .news-rule { border-top: 1px dotted #c8c8c8; margin-top: 10px; }
  .quick { margin-top: 20px; height: 120px; }
  .quick .panel-title { margin-bottom: 6px; }
  .quick p { margin-top: 0; }
</style>
</head>
<body>
  <div class="page">
    <header class="site-header">
      <div class="brand"><span class="brand-mark"></span><span class="brand-name">Kaito Domains</span></div>
      <div class="languages">
        <span class="language" style="left:597px"><span class="language-flag"></span>English</span>
        <span class="language" style="left:662px"><span class="language-flag"></span>日本語</span>
        <span class="language" style="left:730px"><span class="language-flag"></span>中文</span>
      </div>
    </header>

    <nav class="nav">
      <span class="nav-item" style="left:14px">Home</span>
      <span class="nav-item" style="left:66px">Pricing</span>
      <span class="nav-item" style="left:126px">Search</span>
      <span class="nav-item" style="left:186px">FAQ</span>
      <span class="nav-item" style="left:226px">Hosting in Japan</span>
      <span class="nav-item" style="left:350px">Resellers</span>
      <span class="nav-item" style="left:427px">Contact Us</span>
      <span class="control-panel">Control Panel</span>
    </nav>

    <div class="crumbs">
      <span class="crumbs-trail"><a>Control Panel</a> &gt; Search Domain</span>
      <span class="crumbs-account"><a>Login Here</a> / Create a new account <strong><a>HERE</a></strong></span>
    </div>

    <section class="search-area">
      <h1 class="search-title">Domain Search Availability</h1>
      <p class="search-intro">To search for multiple domains, please enter the domains in the textarea below.<br>If the domain is available, you may continue to register the domain. If the domain is unavailable, please search for an alternate domain.</p>
    </section>

    <input class="domain-input" type="text" value="mywebsite">

    <svg class="tld-chain" width="260" height="400" viewBox="0 0 260 400" aria-label="Domain extension selector">
      <defs>
        <polygon id="hex" points="0,-19 16.5,-9.5 16.5,9.5 0,19 -16.5,9.5 -16.5,-9.5"/>
      </defs>
      <g stroke="var(--hex-stroke)" stroke-width="1" fill="#fff">
        <use href="#hex" x="32" y="377"/>
        <use href="#hex" x="61" y="360"/>
        <use href="#hex" x="90" y="344"/>
        <use href="#hex" x="118" y="328" fill="var(--hex-active)"/>
        <use href="#hex" x="146" y="312"/>
        <use href="#hex" x="174" y="296"/>
        <use href="#hex" x="202" y="280"/>
        <use href="#hex" x="230" y="264"/>
      </g>
      <text x="32" y="380">info</text>
      <text x="61" y="363">asia</text>
      <text x="90" y="347">biz</text>
      <text x="118" y="331" style="fill:#666;font-weight:400">org</text>
      <text x="146" y="315">com</text>
      <text x="174" y="299">net</text>
      <text x="202" y="283">gov</text>
      <text x="230" y="267">jp</text>
    </svg>

    <div class="concept-sketch" style="left:40px;top:457px;width:117px;height:108px" role="img" aria-label="Layout sketch: extensions grouped as stacked cubes"></div>
    <div class="concept-sketch" style="left:183px;top:457px;width:131px;height:129px" role="img" aria-label="Layout sketch: extensions grouped as packed circles"></div>
    <div class="concept-sketch" style="left:340px;top:441px;width:158px;height:159px" role="img" aria-label="Layout sketch: extensions grouped in a triangle grid"></div>

    <aside class="sidebar">
      <div class="promo">
        <span class="promo-globe" role="img" aria-label="Globe illustration"></span>
        .JP domain<br>Transfers<br>are free.
        <span class="promo-button">Contact us for info</span>
      </div>

      <div class="panel news">
        <div class="panel-head">
          <div class="panel-title">Site News</div>
          <span class="badge-new"></span>
          <span class="panel-icon" role="img" aria-label="News folder icon"></span>
        </div>
        <p><span class="highlight">Discount .NE.JP domains</span> are now available! Lots of untouched .NE.JP domains still available!</p>
        <p>KaitoDomains.com is a <strong>Japan domain registrar</strong> certified by the NDRA</p>
        <div class="news-rule"></div>
      </div>

      <div class="panel quick">
        <div class="panel-title">Quick Question</div>
        <p>Do you have a questions about the JP domain? Please feel free to ask us.</p>
      </div>
    </aside>
  </div>
</body>
</html>
```